Trucking company specializing in intermodal containers

We need a logo design for our trucking company based in Kent, Washington. Our companies name is Varnell Haulways LLC, we specialize in intermodal containers, and work off of the Crestmark Rail Lines and the ports. We provide service by transporting freight with our fleet of trucks. We operate within Washington, Oregon, and Idaho. Our fleet consists of an east division and a local division. Our team motto currently is globally connected, locally invested.

Target Market(s)

brokers, intermodal management companies, customers

Industry/Entity Type

Trucking Company

Contact Information for Business Card

physical address 4153 N. 318th Pl Kent, WA 98417
office number is 253-555-0148

Font styles to use
Sans Serif

Colors

Designer to choose colors to be used in the design.

Requirements
Must have
• We need to update our current logo. Something like an emblem; that makes a statement that this logo/ sign represents Varnell Haulways. Something like a royal stamp but in this case a royal shield.
Nice to have
• simple, yet bold. something someone does not currently have. We need something fresh and exciting. Something that will also make a statement because currently our reputation is great within the industry and our community. But we need to reflect that we are professional and willing to provide the best service. We are open to new statement lines.
Should not have
• Should not have something thats been used before. We are open to suggestions that you have and a design that is completely unique and you make originally without what we want but what you like as well. Ofcourse it should still represent the industry we are in.

```html
<!DOCTYPE html>
<html lang="en">
<head>
<meta charset="utf-8">
<title>Varnell Haulways LLC – Business Card</title>
<link href="https://fonts.googleapis.com/css2?family=Tinos:wght@400;700&family=Open+Sans:wght@400&display=swap" rel="stylesheet">
<style>
  :root {
    --backdrop: #d2dcdc;
    --orange: #ec5704;
    --ink: #060807;
    --paper: #ffffff;
    --ghost: #e6e6e6;
    --caption: #555c5c;
  }
  * { margin: 0; padding: 0; box-sizing: border-box; }
  html, body { width: 1200px; height: 1200px; overflow: hidden; }
  body {
    background: var(--backdrop);
    position: relative;
    font-family: "Tinos", "Times New Roman", serif;
  }
  .card {
    position: absolute;
    width: 674px;
    height: 386px;
    overflow: hidden;
  }
  /* Front */
  .card-front { left: 133px; top: 165px; background: var(--paper); }
  .band-orange { position: absolute; left: 0; top: 0; width: 134px; height: 100%; background: var(--orange); }
  .band-black { position: absolute; left: 134px; top: 0; width: 62px; height: 100%; background: var(--ink); }
  .tab-orange { position: absolute; left: 134px; top: 166px; width: 62px; height: 53px; background: var(--orange); }
  .tab-mark {
    position: absolute; left: 5px; top: 10px; width: 52px; height: 33px;
    background: linear-gradient(180deg, #3a2a20, #1a1410); border-radius: 3px;
  }
  .bg-vehicle {
    position: absolute; left: 210px; top: 80px; width: 460px; height: 306px;
    background: radial-gradient(ellipse at 55% 50%, var(--ghost) 0%, rgba(230,230,230,0.5) 55%, rgba(255,255,255,0) 80%);
  }
  .person-name {
    position: absolute; left: 232px; top: 170px;
    font-size: 42px; font-weight: 400; color: var(--ink); letter-spacing: -0.5px;
  }
  .person-title {
    position: absolute; left: 333px; top: 226px;
    font-size: 13px; letter-spacing: 4.5px; color: var(--orange);
  }
  /* Back */
  .card-back { left: 389px; top: 586px; background: var(--ink); }
  .tab-white { position: absolute; left: 306px; top: 0; width: 61px; height: 64px; background: var(--paper); }
  .company-name {
    position: absolute; left: 0; right: 0; top: 146px; text-align: center;
    font-size: 40px; font-weight: 700; color: var(--paper); letter-spacing: 1px;
  }
  .contact { position: absolute; top: 290px; width: 240px; text-align: center; color: var(--paper); }
  .contact svg { display: block; margin: 0 auto 12px; width: 16px; height: 16px; }
  .contact-phone { left: -11px; font-size: 21px; top: 288px; }
  .contact-address { left: 211px; font-size: 15px; top: 290px; }
  .contact-web { left: 434px; font-size: 15px; top: 290px; }
  .contact-phone svg { margin-bottom: 8px; }
  .caption {
    position: absolute; right: 33px; top: 1144px;
    font-family: "Open Sans", Arial, sans-serif; font-size: 20px;
    color: var(--caption); letter-spacing: 1px;
  }
</style>
</head>
<body>
  <section class="card card-front">
    <div class="band-orange"></div>
    <div class="band-black"></div>
    <div class="tab-orange"><div class="tab-mark" role="img" aria-label="Small delivery truck illustration"></div></div>
    <div class="bg-vehicle" role="img" aria-label="Faint large delivery truck illustration"></div>
    <h1 class="person-name">YOUR NAME</h1>
    <p class="person-title">DESIGNATION</p>
  </section>

  <section class="card card-back">
    <div class="tab-white"></div>
    <h2 class="company-name">VARNELL HAULWAYS LLC</h2>

    <div class="contact contact-phone">
      <svg viewBox="0 0 24 24" aria-hidden="true"><path fill="#ec5704" d="M6.6 10.8a15 15 0 0 0 6.6 6.6l2.2-2.2a1 1 0 0 1 1-.25 11.4 11.4 0 0 0 3.6.57 1 1 0 0 1 1 1V20a1 1 0 0 1-1 1A17 17 0 0 1 3 4a1 1 0 0 1 1-1h3.5a1 1 0 0 1 1 1c0 1.25.2 2.45.57 3.57a1 1 0 0 1-.25 1z"/></svg>
      253-555-0148
    </div>
    <div class="contact contact-address">
      <svg viewBox="0 0 24 24" aria-hidden="true"><path fill="#ec5704" d="M12 2a7 7 0 0 0-7 7c0 5.2 7 13 7 13s7-7.8 7-13a7 7 0 0 0-7-7zm0 9.5A2.5 2.5 0 1 1 12 6.5a2.5 2.5 0 0 1 0 5z"/></svg>
      4153 N. 318th Pl Kent, WA 98417
    </div>
    <div class="contact contact-web">
      <svg viewBox="0 0 24 24" aria-hidden="true"><g fill="none" stroke="#ec5704" stroke-width="2"><circle cx="12" cy="12" r="9"/><ellipse cx="12" cy="12" rx="4" ry="9"/><path d="M3 12h18M4.5 7.5h15M4.5 16.5h15"/></g></svg>
      www.varnellhaulwaysllc.com.
    </div>
  </section>

  <p class="caption">Varnell Haulways LLC_B Card 4</p>
</body>
</html>
```